marlow keyhaven.com

we are a new company that offer people that have lost there bit coin transaction a recovery and retrieval service
We are looking for a website that will allow you to fill in your details

name
email
bitcoins or other crypto lost and date of transaction

and then an auto reply to them from a given email to verify there email

I am looking for an easy for the client to leave there interest and has a security look around it and looks familiar to the user.

https://tandrelpath.info/?gclid=Xq7LmPzTgRWbNcEvHsKyDa3UjFoeIq92hQ4nBvtzYc5rWpLm8-k2-fAdGxuoTjQe_NsVbHwMzYqEcPlKrUsDa_qwXz

https://osmerlinkgroup.com

https://www.frendaxo.com/faq-items/restoring-your-account-access/

Target Market(s)

early investors into crypto

Industry/Entity Type

It Company

Logo Text

MARLOW KEYHAVEN/FINDERS

Coding

Coded - Design and coding required

Number of Pages Required

3 page

Requirements
Must have
• be able to :
• complete
• Name,
• Email
• transaction date of exchange and how much they invested

```html
<!DOCTYPE html>
<html lang="en">
<head>
<meta charset="utf-8">
<title>Marlow Keyhaven – Recovering your bitcoin wallet</title>
<link href="https://fonts.googleapis.com/css2?family=Open+Sans:wght@400;600;700;800&display=swap" rel="stylesheet">
<style>
:root{
  --gold:#c9a53a;
  --gold-light:#e2c25a;
  --gold-deep:#a88620;
  --ink:#1c1c1c;
  --text:#555;
  --muted:#8a8a8a;
  --panel:#ececec;
  --field:#ffffff;
  --white:#ffffff;
  --line:#d9d9d9;
}
*{box-sizing:border-box;margin:0;padding:0}
html,body{width:1200px;height:4018px;overflow:hidden}
body{font-family:"Open Sans",Arial,sans-serif;color:var(--text);background:var(--white);font-size:14px}
.page{width:1200px;height:4018px;position:relative}

/* Header */
.site-header{height:120px;position:relative;background:var(--white)}
.topbar{position:absolute;right:0;top:0;width:500px;height:44px;background:var(--gold);display:flex;align-items:center;justify-content:flex-end;gap:22px;padding-right:22px;color:var(--white);font-size:13px;font-weight:600}
.topbar .item{display:flex;align-items:center;gap:7px}
.topbar .socials{display:flex;gap:6px}
.dot{width:22px;height:22px;border-radius:50%;border:1.5px solid var(--white);display:inline-block}
.brand{position:absolute;left:38px;top:42px;display:flex;align-items:center;gap:12px}
.brand-mark{width:62px;height:62px;border-radius:50%;background:var(--ink)}
.brand-name{font-size:33px;font-weight:700;color:var(--ink);letter-spacing:.5px;text-transform:uppercase}
.nav{position:absolute;right:20px;top:68px;display:flex;gap:6px}
.nav a{font-size:14px;font-weight:700;color:var(--ink);text-decoration:none;text-transform:uppercase;padding:8px 12px;border:2px solid transparent}
.nav a.active{border-color:var(--gold);color:var(--gold)}

/* Hero */
.hero{height:604px;position:relative;background:radial-gradient(ellipse at 50% 78%,#fff3c8 0%,#f4b93a 18%,#c77a10 42%,#5a3406 72%,#2a1703 100%);display:flex;flex-direction:column;align-items:center}
.hero h1{margin-top:212px;color:var(--white);font-size:54px;font-weight:700;letter-spacing:.3px}
.btn-outline{margin-top:34px;width:214px;height:52px;border:3px solid var(--white);background:var(--gold);color:var(--white);font-size:22px;font-weight:700;display:flex;align-items:center;justify-content:center;text-transform:uppercase;border-radius:3px}

/* Section title */
.section-title{display:flex;align-items:center;gap:14px}
.section-title .rule{height:2px;width:62px;background:var(--ink)}
.section-title .badge{width:62px;height:62px;border-radius:50%;border:3px solid var(--ink);background:var(--white)}
.section-title h2{font-size:25px;font-weight:700;color:var(--ink);text-transform:uppercase}
.section-title h2 span{color:var(--gold)}
.section-title.centered{justify-content:center}

/* About */
.about{height:629px;position:relative}
.about-copy{position:absolute;left:88px;top:100px;width:527px}
.about-copy p{margin-top:58px;font-size:14px;line-height:21px;color:var(--text)}
.more-btn{display:flex;align-items:center;margin-top:38px}
.more-btn .disc{width:52px;height:52px;border-radius:50%;background:var(--gold);border:4px solid var(--ink);display:flex;align-items:center;justify-content:center;position:relative;z-index:1}
.more-btn .pill{height:36px;width:180px;margin-left:-20px;background:var(--ink);color:var(--white);font-size:14px;font-weight:700;display:flex;align-items:center;justify-content:center;border-radius:0 8px 8px 0;padding-left:18px}

.recover-form{position:absolute;left:732px;top:93px;width:380px;height:443px;background:var(--panel)}
.form-banner{position:absolute;left:-12px;top:0;width:404px;height:54px;background:var(--gold);color:var(--ink);font-size:17px;font-weight:800;text-transform:uppercase;display:flex;align-items:center;justify-content:center}
.form-banner::before,.form-banner::after{content:"";position:absolute;bottom:-12px;border-top:12px solid var(--gold-deep)}
.form-banner::before{left:0;border-left:12px solid transparent}
.form-banner::after{right:0;border-right:12px solid transparent}
.form-body{position:absolute;left:40px;top:74px;width:316px;display:flex;flex-direction:column;gap:9px}
.field{height:34px;background:var(--field);font-size:12px;font-weight:600;color:#333;display:flex;align-items:center;justify-content:space-between;padding:0 10px}
.field-row{display:flex;gap:8px}
.field-row .field{flex:1}
.field.area{height:84px;align-items:flex-start;padding-top:10px}
.submit{width:134px;height:34px;background:var(--ink);color:var(--white);font-size:14px;font-weight:700;display:flex;align-items:center;justify-content:center;margin-top:12px;text-transform:uppercase}

/* FAQ */
.faq{height:898px;position:relative;background:linear-gradient(90deg,var(--gold) 0%,var(--gold) 48%,#e8d9a6 62%,#dfe7ea 72%,#cfdbe0 100%);overflow:hidden}
.faq-photo{position:absolute;right:0;top:0;width:560px;height:898px;background:linear-gradient(180deg,#e9eef0 0%,#d5e0e4 55%,#b9c8cc 100%);opacity:.55}
.faq .section-title{position:absolute;left:140px;top:90px}
.faq .section-title .rule{background:var(--white)}
.faq .section-title h2 span{color:var(--white)}
.faq-list{position:absolute;left:88px;top:196px;width:582px;display:flex;flex-direction:column;gap:13px}
.faq-item{background:var(--white);border-radius:10px;padding:0 16px;min-height:35px;box-shadow:0 1px 3px rgba(0,0,0,.15)}
.faq-q{height:35px;display:flex;align-items:center;justify-content:space-between;font-size:14px;font-weight:700;color:var(--ink)}
.faq-a{font-size:13px;line-height:19px;color:var(--text);padding-bottom:12px}

/* Testimonials */
.testimonials{height:509px;position:relative}
.testimonials .section-title{position:absolute;left:0;right:0;top:91px}
.quotes{position:absolute;left:88px;top:193px;display:flex;gap:27px}
.quote{width:322px;position:relative}
.quote-box{height:172px;background:var(--panel);padding:24px 22px 0 64px;font-size:14px;line-height:21px;color:var(--text);position:relative}
.quote-box::after{content:"";position:absolute;left:30px;bottom:-14px;border-top:14px solid var(--panel);border-right:14px solid transparent}
.quote-mark{position:absolute;left:20px;top:20px;font-size:46px;font-weight:800;color:var(--ink);line-height:40px}
.avatar{position:absolute;right:22px;top:112px;width:94px;height:94px;border-radius:50%;border:4px solid var(--gold);background:linear-gradient(160deg,#f1e6d8,#c9b59c)}
.quote-name{margin-top:24px;font-size:14px;font-weight:700;color:var(--ink)}

/* Articles */
.articles{height:844px;position:relative;background:var(--panel)}
.articles .section-title{position:absolute;left:0;right:0;top:90px}
.articles .section-title .badge{background:var(--panel)}
.article-grid{position:absolute;left:88px;top:201px;width:1024px;height:443px}
.card{position:absolute;background:var(--white)}
.card .photo{width:100%}
.card .tag{position:absolute;left:-10px;top:-12px;width:104px;height:104px;border-radius:50%;background:var(--gold);color:var(--white);font-size:13px;font-weight:700;line-height:16px;display:flex;align-items:center;justify-content:center;text-align:center;padding:10px}
.card p{font-size:13px;line-height:19px;color:var(--text);padding:12px 16px}
.card.big{left:0;top:0;width:327px;height:443px}
.card.big .photo{height:172px;background:linear-gradient(135deg,#dfe6ec,#8fa3b3)}
.card.big p{padding:28px 28px}
.card.small{width:322px;height:202px}
.card.small .photo{height:143px}
.c1{left:349px;top:0}.c1 .photo{background:linear-gradient(135deg,#cfdbe6,#7f9ab1)}
.c2{left:697px;top:0}.c2 .photo{background:linear-gradient(135deg,#b6c6d6,#4e6a86)}
.c3{left:349px;top:228px;height:215px!important}.c3 .photo{background:linear-gradient(135deg,#e5e8ea,#6f7d88)}
.c4{left:697px;top:228px;height:215px!important}.c4 .photo{background:linear-gradient(135deg,#c6d3e0,#5a7590)}
.view-all{position:absolute;left:0;right:0;top:703px;display:flex;justify-content:center}
.view-all .pill{width:150px}

/* Footer */
.site-footer{height:362px;position:relative}
.footer-box{position:absolute;left:94px;top:46px;width:1018px;height:276px;border:3px solid var(--gold)}
.footer-brand{position:absolute;left:34px;top:104px;display:flex;align-items:center;gap:10px}
.footer-brand .brand-mark{width:44px;height:44px}
.footer-brand .brand-name{font-size:23px}
.footer-col{position:absolute;top:46px}
.footer-col h4{font-size:13px;font-weight:700;color:var(--gold);text-transform:uppercase;padding-bottom:8px;border-bottom:1px solid var(--line);width:150px;margin-bottom:12px}
.footer-col ul{list-style:none;font-size:13px;line-height:20px;color:var(--ink)}
.contact-line{display:flex;gap:8px;font-size:12px;line-height:17px;color:var(--ink);margin-bottom:12px}
.contact-line .ico{width:20px;height:20px;border-radius:50%;border:1.5px solid var(--ink);flex:none;display:flex;align-items:center;justify-content:center}
.cta-card{position:absolute;right:32px;top:26px;width:214px;height:186px;background:var(--gold);display:flex;flex-direction:column;align-items:center;padding-top:32px}
.cta-card .cta{width:178px;height:38px;background:var(--ink);color:var(--white);font-size:14px;font-weight:700;text-transform:uppercase;display:flex;align-items:center;justify-content:center}
.cta-card small{margin-top:22px;font-size:11px;font-weight:700;color:var(--white);text-transform:uppercase}
.cta-card .socials{margin-top:8px;display:flex;gap:6px}
.copyright{position:absolute;left:0;bottom:0;width:1200px;height:52px;background:var(--gold);color:var(--ink);font-size:11px;font-weight:600;display:flex;align-items:center;justify-content:center;text-transform:uppercase}
</style>
</head>
<body>
<div class="page">

<header class="site-header">
  <div class="topbar">
    <span class="item">
      <svg width="16" height="16" viewBox="0 0 24 24" fill="#fff"><path d="M6.6 10.8a15.1 15.1 0 0 0 6.6 6.6l2.2-2.2a1 1 0 0 1 1-.25 11.4 11.4 0 0 0 3.6.57 1 1 0 0 1 1 1V20a1 1 0 0 1-1 1A17 17 0 0 1 3 4a1 1 0 0 1 1-1h3.5a1 1 0 0 1 1 1c0 1.25.2 2.45.57 3.57a1 1 0 0 1-.25 1z"/></svg>
      (555) 010-4827
    </span>
    <span class="item">
      <svg width="16" height="16" viewBox="0 0 24 24" fill="none" stroke="#fff" stroke-width="2"><rect x="3" y="5" width="18" height="14" rx="1"/><path d="M3 6l9 7 9-7"/></svg>
      info@marlowkeyhaven.com
    </span>
    <span class="socials"><i class="dot"></i><i class="dot"></i><i class="dot"></i></span>
  </div>
  <div class="brand">
    <span class="brand-mark"></span>
    <span class="brand-name">Marlow Keyhaven</span>
  </div>
  <nav class="nav">
    <a class="active" href="#">Home</a>
    <a href="#">About</a>
    <a href="#">FAQs</a>
    <a href="#">Testimonials</a>
    <a href="#">Articles</a>
    <a href="#">Contact</a>
  </nav>
</header>

<section class="hero" role="img" aria-label="Glowing golden globe covered with a network of connected nodes">
  <h1>Recovering your bitcoin wallet</h1>
  <div class="btn-outline">Get Started</div>
</section>

<section class="about">
  <div class="about-copy">
    <div class="section-title">
      <span class="rule"></span><span class="badge"></span>
      <h2>About <span>Marlow Keyhaven</span></h2>
    </div>
    <p>We help early crypto investors regain access to lost wallets and missing transactions. Our team traces each case with care, using proven recovery methods and strict privacy rules. Tell us what happened, when the transaction took place and how much you invested, and a specialist will review your details. Every enquiry is handled confidentially, and we only ask for the information needed to begin. Most clients hear back from us within one working day with clear next steps.</p>
    <div class="more-btn">
      <span class="disc"><svg width="18" height="18" viewBox="0 0 24 24" fill="#1c1c1c"><path d="M5 19 19 5v10l-4-4-8 8z"/></svg></span>
      <span class="pill">Learn More</span>
    </div>
  </div>

  <form class="recover-form">
    <div class="form-banner">Recover your wallet now!</div>
    <div class="form-body">
      <div class="field">Your Name*</div>
      <div class="field-row"><div class="field">Email Address*</div><div class="field">Phone Number</div></div>
      <div class="field">Transaction Date*
        <svg width="16" height="16" viewBox="0 0 24 24" fill="none" stroke="#333" stroke-width="2"><rect x="3" y="5" width="18" height="16"/><path d="M3 10h18M8 3v4M16 3v4"/></svg>
      </div>
      <div class="field">Amount Invested*
        <svg width="12" height="8" viewBox="0 0 12 8" fill="#333"><path d="M0 0h12L6 8z"/></svg>
      </div>
      <div class="field">What Wallet Did You Use to Store Your Coins?</div>
      <div class="field area">What Problem Are You Having With Your Wallet?</div>
      <div class="submit">Submit</div>
    </div>
  </form>
</section>

<section class="faq">
  <div class="faq-photo" role="img" aria-label="Woman by the sea raising her arms in relief"></div>
  <div class="section-title">
    <span class="rule"></span><span class="badge"></span>
    <h2>Frequently Asked <span>Questions</span></h2>
  </div>
  <div class="faq-list">
    <div class="faq-item"><div class="faq-q">Can you recover my wallet?<svg width="12" height="8" viewBox="0 0 12 8" fill="none" stroke="#1c1c1c" stroke-width="2"><path d="M1 1l5 5 5-5"/></svg></div></div>
    <div class="faq-item">
      <div class="faq-q">Which currencies/wallets can you recover?<svg width="12" height="8" viewBox="0 0 12 8" fill="none" stroke="#1c1c1c" stroke-width="2"><path d="M1 7l5-5 5 5"/></svg></div>
      <div class="faq-a">We work with most major coins and tokens, including bitcoin, ether and litecoin, along with a wide range of desktop, mobile and hardware wallets. If your wallet is older or less common, send us the details anyway. Our specialists review every request and will tell you honestly whether recovery is possible before any work begins, so you always know where you stand.</div>
    </div>
    <div class="faq-item"><div class="faq-q">Why should I trust you?<svg width="12" height="8" viewBox="0 0 12 8" fill="none" stroke="#1c1c1c" stroke-width="2"><path d="M1 1l5 5 5-5"/></svg></div></div>
    <div class="faq-item"><div class="faq-q">Will you keep my coins safe and my information confidential?<svg width="12" height="8" viewBox="0 0 12 8" fill="none" stroke="#1c1c1c" stroke-width="2"><path d="M1 1l5 5 5-5"/></svg></div></div>
    <div class="faq-item"><div class="faq-q">How are you different from other wallet recovery services?<svg width="12" height="8" viewBox="0 0 12 8" fill="none" stroke="#1c1c1c" stroke-width="2"><path d="M1 1l5 5 5-5"/></svg></div></div>
    <div class="faq-item"><div class="faq-q">What happens after you recover my wallet?<svg width="12" height="8" viewBox="0 0 12 8" fill="none" stroke="#1c1c1c" stroke-width="2"><path d="M1 1l5 5 5-5"/></svg></div></div>
    <div class="faq-item"><div class="faq-q">I can't login to my Chainvault wallet. Can you help?<svg width="12" height="8" viewBox="0 0 12 8" fill="none" stroke="#1c1c1c" stroke-width="2"><path d="M1 1l5 5 5-5"/></svg></div></div>
    <div class="faq-item"><div class="faq-q">I need help buying/selling/trading Bitcoin. Can you help?<svg width="12" height="8" viewBox="0 0 12 8" fill="none" stroke="#1c1c1c" stroke-width="2"><path d="M1 1l5 5 5-5"/></svg></div></div>
    <div class="faq-item"><div class="faq-q">Can you help me with Coinmarra, Paytrelle, Krevix, or another exchange?<svg width="12" height="8" viewBox="0 0 12 8" fill="none" stroke="#1c1c1c" stroke-width="2"><path d="M1 1l5 5 5-5"/></svg></div></div>
    <div class="faq-item"><div class="faq-q">How can I contact you securely?<svg width="12" height="8" viewBox="0 0 12 8" fill="none" stroke="#1c1c1c" stroke-width="2"><path d="M1 1l5 5 5-5"/></svg></div></div>
  </div>
</section>

<section class="testimonials">
  <div class="section-title centered">
    <span class="rule"></span><span class="badge"></span>
    <h2>Testimonials</h2>
    <span class="rule"></span>
  </div>
  <div class="quotes">
    <div class="quote">
      <div class="quote-box"><span class="quote-mark">“</span>Quick, honest and careful. They found my lost transfer and kept me updated at every step of the way.</div>
      <div class="avatar" role="img" aria-label="Portrait of client Helena Marsh"></div>
      <div class="quote-name">Helena Marsh</div>
    </div>
    <div class="quote">
      <div class="quote-box"><span class="quote-mark">“</span>I had almost given up on my old wallet. The team was patient and recovered it within a week.</div>
      <div class="avatar" role="img" aria-label="Portrait of client Nadia Corwell"></div>
      <div class="quote-name">Nadia Corwell</div>
    </div>
    <div class="quote">
      <div class="quote-box"><span class="quote-mark">“</span>Clear advice and no pressure. I finally have access to coins I bought years ago. Highly recommended.</div>
      <div class="avatar" role="img" aria-label="Portrait of client Tobias Fenwick"></div>
      <div class="quote-name">Tobias Fenwick</div>
    </div>
  </div>
</section>

<section class="articles">
  <div class="section-title centered">
    <span class="rule"></span><span class="badge"></span>
    <h2>Articles</h2>
    <span class="rule"></span>
  </div>
  <div class="article-grid">
    <article class="card big">
      <div class="photo" role="img" aria-label="Business team smiling around a laptop in an office"></div>
      <span class="tag">How to Become a Powerful Investor</span>
      <p>Smart investing starts with protecting what you already own. Keep your recovery phrases offline, note every transaction date and review your wallets often. Small habits like these make it far easier to act quickly if something ever goes wrong, and they give you the confidence to plan your next move with a clear mind.</p>
    </article>
    <article class="card small c1">
      <div class="photo" role="img" aria-label="Businessman leaping across a bright city backdrop"></div>
      <span class="tag">Become an Inspiration and Rule The World</span>
      <p>Simple daily steps that help you stay focused on long term goals.</p>
    </article>
    <article class="card small c2">
      <div class="photo" role="img" aria-label="Professionals in suits meeting at a desk"></div>
      <span class="tag">Be the Leader You Wish</span>
      <p>Lead with clarity and build trust with every decision you make.</p>
    </article>
    <article class="card small c3">
      <div class="photo" role="img" aria-label="Hand pointing at a market chart on a tablet"></div>
      <span class="tag">Overcome Your Fear</span>
      <p>Learn to manage risk calmly when markets move against you.</p>
    </article>
    <article class="card small c4">
      <div class="photo" role="img" aria-label="Entrepreneur holding a smartphone"></div>
      <span class="tag">Become a Successful Entrepreneur</span>
      <p>What it takes to turn a small idea into a lasting business.</p>
    </article>
  </div>
  <div class="view-all">
    <div class="more-btn" style="margin-top:0">
      <span class="disc"><svg width="18" height="18" viewBox="0 0 24 24" fill="#1c1c1c"><path d="M5 19 19 5v10l-4-4-8 8z"/></svg></span>
      <span class="pill">View All</span>
    </div>
  </div>
</section>

<footer class="site-footer">
  <div class="footer-box">
    <div class="footer-brand">
      <span class="brand-mark"></span>
      <span class="brand-name">Marlow Keyhaven</span>
    </div>
    <div class="footer-col" style="left:352px">
      <h4>Quick Links</h4>
      <ul><li>Home</li><li>About</li><li>FAQs</li><li>Testimonials</li><li>Articles</li><li>Contact</li></ul>
    </div>
    <div class="footer-col" style="left:518px">
      <h4>Quick Links</h4>
      <div class="contact-line"><span class="ico"><svg width="10" height="12" viewBox="0 0 24 30" fill="#1c1c1c"><path d="M12 0a10 10 0 0 0-10 10c0 8 10 20 10 20s10-12 10-20A10 10 0 0 0 12 0zm0 14a4 4 0 1 1 0-8 4 4 0 0 1 0 8z"/></svg></span><span>MARLOW KEYHAVEN<br>27 Ashbury Crescent<br>LEEDS, ENGLAND LS6 4QT</span></div>
      <div class="contact-line"><span class="ico"><svg width="10" height="10" viewBox="0 0 24 24" fill="#1c1c1c"><path d="M6.6 10.8a15.1 15.1 0 0 0 6.6 6.6l2.2-2.2a1 1 0 0 1 1-.25 11.4 11.4 0 0 0 3.6.57 1 1 0 0 1 1 1V20a1 1 0 0 1-1 1A17 17 0 0 1 3 4a1 1 0 0 1 1-1h3.5a1 1 0 0 1 1 1c0 1.25.2 2.45.57 3.57a1 1 0 0 1-.25 1z"/></svg></span><span>(555) 010-4827</span></div>
      <div class="contact-line"><span class="ico"><svg width="10" height="10" viewBox="0 0 24 24" fill="none" stroke="#1c1c1c" stroke-width="3"><rect x="3" y="5" width="18" height="14"/><path d="M3 6l9 7 9-7"/></svg></span><span>info@marlowkeyhaven.com</span></div>
    </div>
    <div class="cta-card">
      <div class="cta">Request More Info</div>
      <small>Connect With Us</small>
      <div class="socials"><i class="dot"></i><i class="dot"></i><i class="dot"></i></div>
    </div>
  </div>
  <div class="copyright">Copyright © 2018 Marlow Keyhaven. All rights reserved.</div>
</footer>

</div>
</body>
</html>
```